Tilda Tinkerwire, An IT Company Has New Logo, Need Fresh Business Cards

IT company is called Tilda Tinkerwire and is displayed nicely with the new logo from here on pitchloft. Would like a fresh business card look that encompasses the idea that we want clients to Cherish Every Gadget. I love the use of circuitry with hearts as endpoints and x's and o's. It needs to have room for my certification logos of which there are 4 and a BRJ Alumni log. I am attaching my current card to illustrate how it has always captured attention, but that was in the early stages of business when I was doing more residential work. I am focused on businesses now, so a level of professionalism is necessary. I would also like the card to lend itself well to additional stationary, email signature, ticketing template for my workboard, etc. For the time being, I need the card for an upcoming conference so that work will come later. Color scheme should be that of the new logo. Thank you and I look forward to the designs.

Target Market(s)

Businesses looking for IT services.

Industry/Entity Type

Information Technology

Contact Information for Business Card

See above

Requirements
Must have
• New logo colors and a warm feel. Possibly a tad feminine as I am female, but appealing to males.
Nice to have
• I would like techy, but no too much so. I like friendly and connecting feels. People LOVED my old card and called me because it gave them a warm feeling.

```html
<!DOCTYPE html>
<html lang="en">
<head>
<meta charset="utf-8">
<title>Tilda Tinkerwire — Business Cards</title>
<link rel="stylesheet" href="https://fonts.googleapis.com/css2?family=Open+Sans:wght@400;600;700&display=swap">
<style>
  :root {
    --bg: #e6e6e4;
    --paper: #ffffff;
    --charcoal: #2b2b2c;
    --ink: #1d1d1f;
    --sky: #5fc3dc;
    --sky-soft: #a9dbe6;
    --pink: #e46aa8;
    --lime: #b6cf3c;
    --edge: #b0457f;
    --muted-light: #e8e8e8;
  }
  * { box-sizing: border-box; margin: 0; padding: 0; }
  html, body { width: 1200px; height: 1021px; overflow: hidden; }
  body {
    background: var(--bg);
    font-family: "Open Sans", sans-serif;
    position: relative;
  }
  .card {
    position: absolute;
    width: 620px;
    height: 354px;
    border-bottom: 6px solid var(--edge);
    box-shadow: 0 10px 24px rgba(0,0,0,.18);
  }
  /* Front card */
  .card-front { left: 70px; top: 90px; background: var(--paper); color: var(--ink); }
  .front-brand {
    position: absolute; right: 36px; top: 44px; text-align: right;
  }
  .brand-line { display: flex; align-items: center; gap: 10px; justify-content: flex-end; }
  .brand-dot { width: 16px; height: 16px; border-radius: 50%; background: var(--pink); }
  .brand-name { font-size: 24px; font-weight: 400; color: var(--sky); letter-spacing: -.3px; }
  .brand-tag { font-size: 9px; letter-spacing: 3px; color: var(--pink); text-transform: uppercase; margin-top: 2px; }

  .identity { position: absolute; left: 34px; top: 120px; padding-left: 16px; }
  .identity::before {
    content: ""; position: absolute; left: 0; top: 4px; width: 6px; height: 44px; background: var(--sky-soft);
  }
  .person-name { font-size: 24px; font-weight: 400; line-height: 1.1; }
  .person-name b { font-weight: 700; }
  .job-title { font-size: 12px; color: var(--pink); }

  .contact { position: absolute; left: 50px; top: 220px; }
  .call-label { font-size: 15px; color: var(--sky); line-height: 1.1; }
  .phone { font-size: 26px; font-weight: 400; line-height: 1.15; }
  .contact-lines { margin-top: 12px; font-size: 13px; line-height: 1.75; }
  .contact-row { display: flex; align-items: center; gap: 9px; }
  .contact-row svg { width: 14px; height: 14px; flex: none; }

  .cert-note {
    position: absolute; right: 36px; bottom: 96px; font-size: 13px; color: var(--ink);
  }

  /* Back card */
  .card-back { left: 510px; top: 560px; background: var(--charcoal); color: var(--muted-light); }
  .back-brand {
    position: absolute; left: 0; right: 0; top: 120px; text-align: center;
  }
  .back-brand .brand-line { justify-content: center; gap: 14px; }
  .back-brand .brand-dot { width: 22px; height: 22px; }
  .back-brand .brand-name { font-size: 38px; }
  .back-brand .brand-tag { font-size: 11px; letter-spacing: 5px; margin-top: 4px; }
  .services { margin-top: 18px; font-size: 15px; color: var(--muted-light); }
  .services span { padding: 0 8px; }
</style>
</head>
<body>

  <section class="card card-front" aria-label="Business card front">
    <div class="front-brand">
      <div class="brand-line">
        <span class="brand-dot"></span>
        <span class="brand-name">Tilda Tinkerwire</span>
      </div>
      <div class="brand-tag">Cherish Every Gadget</div>
    </div>

    <div class="identity">
      <div class="person-name">Your <b>Name</b></div>
      <div class="job-title">Job Title</div>
    </div>

    <div class="contact">
      <div class="call-label">Call Tilda</div>
      <div class="phone">555-014-2298</div>
      <div class="contact-lines">
        <div class="contact-row">
          <svg viewBox="0 0 16 16" aria-hidden="true" fill="none" stroke="#6b6b6b" stroke-width="1.2">
            <circle cx="8" cy="8" r="6.5"/><ellipse cx="8" cy="8" rx="3" ry="6.5"/><line x1="1.5" y1="8" x2="14.5" y2="8"/>
          </svg>
          <span>www.tilda-tinkerwire.com</span>
        </div>
        <div class="contact-row">
          <svg viewBox="0 0 16 16" aria-hidden="true" fill="none" stroke="#6b6b6b" stroke-width="1.2">
            <rect x="1.5" y="3.5" width="13" height="9"/><polyline points="1.5,3.5 8,9 14.5,3.5"/>
          </svg>
          <span>hello@tilda-tinkerwire.com</span>
        </div>
      </div>
    </div>

    <div class="cert-note">Four certification logo here</div>
  </section>

  <section class="card card-back" aria-label="Business card back">
    <div class="back-brand">
      <div class="brand-line">
        <span class="brand-dot"></span>
        <span class="brand-name">Tilda Tinkerwire</span>
      </div>
      <div class="brand-tag">Cherish Every Gadget</div>
      <div class="services">Desktops<span>|</span>Laptops<span>|</span>Tablets</div>
    </div>
  </section>

</body>
</html>
```